742 Process Infographic Redesign

We need a redesign of our companies reconstruction process chart that is posted in our construction offices. We would like the design to use flowchart or decision tree in functional approach. This will be used in large format poster as well as on pdfs so will need to be bold yet clear in communication.

Industry/Entity Type

Construction

Font styles to use
Sans Serif

Colors
EE7325
F08F49
F5BC92
FAE3D3
FDF4ED

Requirements
Must have
• same info presented in current design

```html
<!DOCTYPE html>
<html lang="en">
<head>
<meta charset="utf-8">
<title>742 Process</title>
<link href="https://fonts.googleapis.com/css2?family=Archivo+Black&family=Poppins:ital,wght@0,400;0,500;0,600;0,700;0,800;1,400&display=swap" rel="stylesheet">
<style>
:root{
  --recon:#E8505B;
  --accounting:#1A9E97;
  --estimator:#4DBDE9;
  --pm:#FDB515;
  --gm:#D4601A;
  --inactive:#1E64B4;
  --peach:#FAE3D3;
  --grey:#E3E3E3;
  --ink:#1d1d1d;
  --orange:#D4601A;
  --green:#4C9A2A;
  --no:#E0262B;
}
*{box-sizing:border-box;margin:0;padding:0}
html,body{width:1200px;height:1200px;overflow:hidden;background:#fff}
body{font-family:"Poppins",sans-serif;color:var(--ink);position:relative}
.poster{position:absolute;left:0;top:139px;width:1770px;height:1360px;transform:scale(.67797);transform-origin:0 0;background:#fff}
.brand{position:absolute;left:126px;top:92px;display:flex;align-items:center;gap:14px;font-weight:700;font-size:36px;color:var(--orange);letter-spacing:1px}
.brand-square{width:40px;height:40px;background:var(--orange)}
.title{position:absolute;right:91px;top:70px;font-family:"Archivo Black",sans-serif;font-size:104px;letter-spacing:2px;line-height:1.1;font-weight:400}
.title .accent{color:var(--orange);margin-left:30px}
.band{position:absolute;left:127px;width:1557px;border-radius:22px}
.band.peach{background:var(--peach)}
.band.grey{background:var(--grey)}
.band-label{position:absolute;left:0;top:0;bottom:0;width:35px;border-radius:18px;color:#fff;font-weight:600;font-size:26px;writing-mode:vertical-rl;transform:rotate(180deg);display:flex;align-items:center;justify-content:center;letter-spacing:.5px}
.box{position:absolute;border:5px solid var(--c);border-radius:11px;background:linear-gradient(#fff 45%,#e6e6e6);box-shadow:0 3px 5px rgba(0,0,0,.28);display:flex;align-items:center;justify-content:center;text-align:center;font-size:13.5px;line-height:1.22;padding:3px 5px;overflow:hidden}
.box p{display:block;width:100%}
.box.big{border-width:9px;font-size:15px}
.box b{font-weight:700}
.box .head{display:block;font-weight:700;font-size:16px;margin-bottom:8px}
.box small{font-size:10.5px;display:block}
.box i{font-size:12px}
.recon{--c:var(--recon)}.accounting{--c:var(--accounting)}.estimator{--c:var(--estimator)}.pm{--c:var(--pm)}.gm{--c:var(--gm)}.inactive{--c:var(--inactive)}
.decision{position:absolute;clip-path:polygon(50% 0,100% 50%,50% 100%,0 50%);display:flex;align-items:center;justify-content:center;text-align:center;font-size:11px;line-height:1.15;color:#fff}
.decision.green{background:var(--green)}
.decision.red{background:var(--recon);font-weight:700;font-size:15px}
.decision.yellow{background:var(--pm);color:#3a2a00}
.decision.teal{background:var(--accounting)}
.tag{position:absolute;font-size:10px;transform:translateX(-50%)}
.tag.yes{color:var(--green)}
.tag.no{color:var(--no)}
.tag.big{font-size:15px}
.connectors{position:absolute;left:0;top:0;width:1770px;height:1360px;pointer-events:none}
.connectors polyline{fill:none;stroke:#8a8a8a;stroke-width:1.4;marker-end:url(#tip)}
.connectors .neg{stroke:var(--no);marker-end:url(#tipRed)}
.connectors .pos{stroke:var(--green);marker-end:url(#tipGreen)}
.legend{position:absolute;left:126px;top:1262px;display:flex;align-items:center;font-size:21px}
.legend h2{font-weight:700;font-size:28px;margin-right:38px}
.legend-item{display:flex;align-items:center;margin-right:38px}
.swatch{width:30px;height:30px;border-radius:9px;margin-right:10px;background:var(--c)}
</style>
</head>
<body>
<div class="poster">
  <div class="brand"><span class="brand-square"></span>742 CONSTRUCTION</div>
  <h1 class="title">742<span class="accent">PROCESS</span></h1>

  <div class="band peach" style="top:205px;height:245px"><div class="band-label" style="background:var(--green)">Initiation</div></div>
  <div class="band grey" style="top:458px;height:250px"><div class="band-label" style="background:#E06A1F">Planning</div></div>
  <div class="band peach" style="top:731px;height:252px"><div class="band-label" style="background:#222">Execution</div></div>
  <div class="band grey" style="top:1001px;height:242px"><div class="band-label" style="background:var(--inactive)">Closeout</div></div>

  <svg class="connectors" viewBox="0 0 1770 1360">
    <defs>
      <marker id="tip" markerWidth="7" markerHeight="7" refX="6" refY="3.5" orient="auto"><path d="M0,0L7,3.5L0,7z" fill="#8a8a8a"/></marker>
      <marker id="tipRed" markerWidth="7" markerHeight="7" refX="6" refY="3.5" orient="auto"><path d="M0,0L7,3.5L0,7z" fill="#E0262B"/></marker>
      <marker id="tipGreen" markerWidth="7" markerHeight="7" refX="6" refY="3.5" orient="auto"><path d="M0,0L7,3.5L0,7z" fill="#4C9A2A"/></marker>
    </defs>
    <polyline points="290,278 290,294"/>
    <polyline points="379,370 404,370 404,260 432,260"/>
    <polyline points="501,287 501,304"/>
    <polyline points="501,356 501,374"/>
    <polyline points="541,332 606,332"/>
    <polyline points="572,400 590,400 590,385 606,385"/>
    <polyline points="817,332 857,332"/>
    <polyline points="1157,278 1178,278"/>
    <polyline points="1157,375 1178,375"/>
    <polyline points="1317,278 1347,278"/>
    <polyline points="1473,365 1499,365"/>
    <polyline class="neg" points="1583,326 1583,274"/>
    <polyline points="1583,432 1583,456 271,456 271,472"/>
    <polyline points="272,581 272,603"/>
    <polyline points="339,662 502,662 502,637"/>
    <polyline points="631,567 659,567"/>
    <polyline points="759,540 759,530 870,530"/>
    <polyline points="989,655 1087,655 1087,635"/>
    <polyline points="1089,541 1089,518 1186,518"/>
    <polyline points="1226,558 1226,603"/>
    <polyline points="1226,673 1226,690 1279,690"/>
    <polyline points="1372,582 1372,569"/>
    <polyline points="1469,525 1496,525"/>
    <polyline points="1572,593 1572,612"/>
    <polyline points="1572,694 1572,720 270,720 270,744"/>
    <polyline points="270,826 270,848"/>
    <polyline points="336,880 350,880 350,860 365,860"/>
    <polyline points="424,829 424,817"/>
    <polyline points="424,891 424,900"/>
    <polyline points="479,780 506,780"/>
    <polyline points="572,810 572,820"/>
    <polyline points="572,900 572,909"/>
    <polyline points="635,940 655,940 655,787 679,787"/>
    <polyline points="752,830 752,833"/>
    <polyline points="816,860 850,860"/>
    <polyline points="987,860 1022,860"/>
    <polyline points="1092,837 1092,830"/>
    <polyline points="750,883 750,888"/><polyline points="920,883 920,888"/><polyline points="1093,883 1093,888"/>
    <polyline points="750,928 750,931"/><polyline points="920,928 920,931"/><polyline points="1093,928 1093,931"/>
    <polyline points="1159,776 1206,776"/>
    <polyline class="neg" points="1310,776 1422,776 1422,790"/>
    <polyline points="1260,802 1260,808"/>
    <polyline points="1260,873 1260,875"/>
    <polyline points="1260,923 1260,926"/>
    <polyline class="pos" points="1422,868 1422,890"/>
    <polyline points="1487,924 1497,924 1497,795 1513,795"/>
    <polyline points="1583,836 1583,855"/>
    <polyline points="1583,926 1583,993 294,993 294,1012 246,1012 246,1031"/>
    <polyline points="294,1012 342,1012 342,1031"/>
    <polyline points="342,1106 342,1131"/>
    <polyline class="neg" points="381,1159 424,1159 424,1067 468,1067"/>
    <polyline class="pos" points="343,1183 343,1208 450,1208 450,1168 468,1168"/>
    <polyline points="535,1130 535,1107"/>
    <polyline points="598,1067 656,1067"/>
    <polyline points="724,1105 724,1132"/>
    <polyline points="789,1068 801,1068"/>
    <polyline class="pos" points="965,1068 973,1068"/>
    <polyline class="neg" points="885,1108 885,1124"/>
    <polyline points="1120,1063 1146,1063"/>
    <polyline points="1293,1063 1323,1063"/>
    <polyline points="1471,1063 1495,1063"/>
    <polyline points="1561,1096 1561,1124"/>
    <polyline points="958,1169 1024,1169"/>
    <polyline points="1167,1162 1214,1162"/>
  </svg>

  <!-- Initiation -->
  <div class="box gm" style="left:207px;top:235px;width:172px;height:43px;font-size:20px;font-weight:600"><p>New Lead</p></div>
  <div class="box recon" style="left:202px;top:298px;width:177px;height:130px;font-size:13.5px"><p>Enter into <b>TaskBase</b><br>Create <b>FileBox</b><br>Folder<br>Setup <b>SiteSnap</b><br>Date Received</p></div>
  <div class="box pm" style="left:436px;top:229px;width:136px;height:58px;font-size:11.5px"><p>Contact Lead<br>Lead Contacted</p></div>
  <div class="decision green" style="left:461px;top:308px;width:80px;height:48px;font-size:8px;font-weight:700">RESTOREPRO</div>
  <div class="box pm" style="left:436px;top:378px;width:136px;height:57px;font-size:11px"><p>Coordinate with<br><b>Mitigation Manager</b></p></div>
  <div class="box pm big" style="left:610px;top:242px;width:207px;height:169px"><p><span class="head">SITE INSPECTION</span>Scope Sheets,<br>PlanSketch &amp;<br>Interim Agreement<br>Site Inspected</p></div>
  <div class="box estimator big" style="left:861px;top:242px;width:296px;height:169px"><p><span class="head">ESTIMATE CREATION</span>Scope Sheets,<br>PlanSketch &amp;<br>Interim Agreement<br>Site Inspected</p></div>
  <div class="box pm" style="left:1182px;top:252px;width:135px;height:56px;font-size:11px"><p>Estimate<br>Review</p></div>
  <div class="box gm" style="left:1182px;top:344px;width:135px;height:58px;font-size:10.5px"><p>Estimate<br>Approval by<br>GM if &gt; $75K</p></div>
  <div class="box pm" style="left:1351px;top:243px;width:122px;height:168px;border-width:7px;font-size:11px;align-items:flex-start;padding-top:14px"><p><b style="font-size:15px">SUBMIT<br>ESTIMATE</b><br>Customer &amp;<br>Adjuster<br><br><br><i>Estimate<br>Submitted</i></p></div>
  <div class="box gm" style="left:1514px;top:226px;width:136px;height:44px;font-size:10px"><p>Email Notification<br><i style="font-size:10px">Job Not Sold</i></p></div>
  <span class="tag no big" style="left:1581px;top:288px">No</span>
  <div class="decision green" style="left:1503px;top:326px;width:160px;height:78px;font-style:italic;font-size:11.5px">Estimate<br>Submitted</div>
  <span class="tag yes big" style="left:1584px;top:408px">Yes</span>

  <!-- Planning -->
  <div class="box estimator" style="left:205px;top:476px;width:134px;height:105px"><p><b style="font-size:15px">PRINT<br>REPORTS</b><small style="font-size:8.5px">Scope, Components,<br>Summary w/ Detail,<br><b>Approved Estimate</b></small></p></div>
  <div class="box recon" style="left:205px;top:607px;width:134px;height:76px"><p>Create &amp;<br>Share Budget</p></div>
  <div class="box pm big" style="left:367px;top:511px;width:264px;height:122px;font-size:14px"><p>Build <b>Budget</b><br>Develop <b>Payment Schedule</b><br>Create <b>Material Selection Sheet</b></p></div>
  <div class="box pm" style="left:663px;top:540px;width:177px;height:59px"><p>Walk job with Subs<br>and call vendors</p></div>
  <div class="box recon" style="left:874px;top:504px;width:115px;height:66px;font-size:14px"><p>Budget<br>Review</p></div>
  <div class="box gm" style="left:874px;top:592px;width:115px;height:66px;font-size:14px"><p>Budget<br>Review</p></div>
  <div class="box inactive" style="left:1009px;top:541px;width:155px;height:90px"><p>Create<br><b>Work Schedule</b><small>Target Start Date<br>Target Completion</small></p></div>
  <div class="box accounting" style="left:1190px;top:492px;width:73px;height:66px;font-size:9.5px"><p>Invoice<br>Deductible</p></div>
  <div class="box accounting" style="left:1190px;top:607px;width:73px;height:66px;font-size:9.5px"><p>Invoice<br>Deposit</p></div>
  <div class="box gm" style="left:1283px;top:489px;width:186px;height:76px;font-size:16px;font-weight:700"><p>MANAGEMENT<br>REVIEW</p></div>
  <div class="box recon" style="left:1283px;top:582px;width:188px;height:114px;font-size:10.5px"><p><b>Create Customer Packet</b><br>with Work Authorization,<br>Payment Schedule,<br>Mortgage Authorization,<br>Invoices and<br><b>Material Selection Sheet</b></p></div>
  <div class="box pm" style="left:1500px;top:486px;width:145px;height:107px;font-size:15px"><p>CUSTOMER<br><b>ONBOARDING</b><br>MEETING<small style="margin-top:4px">Work Auth &amp; PS</small></p></div>
  <div class="box recon" style="left:1504px;top:616px;width:139px;height:78px;font-size:9.5px"><p>Provide Customer<br>Copies of<br>Onboarding<br>DocsDate</p></div>

  <!-- Execution -->
  <div class="box inactive" style="left:205px;top:748px;width:131px;height:78px"><p>Create<br><b>Purchase Orders</b></p></div>
  <div class="box recon" style="left:205px;top:852px;width:131px;height:90px"><p>Submit WA to<br>Adjuster<br>Requesting<br><b>Depreciation</b></p></div>
  <div class="box recon" style="left:365px;top:747px;width:114px;height:66px"><p>Pull <b>Permit</b><br>if required</p></div>
  <span class="tag no" style="left:424px;top:816px;font-size:8px">No</span>
  <div class="decision red" style="left:369px;top:829px;width:110px;height:62px">&gt; $25,000</div>
  <span class="tag yes" style="left:424px;top:891px;font-size:8px">Yes</span>
  <div class="box recon" style="left:365px;top:904px;width:114px;height:67px"><p>File Signed<br>Contract with<br><b>Courthouse</b></p></div>
  <div class="box pm" style="left:510px;top:751px;width:125px;height:59px;font-size:12px"><p>Initiation<br>Checklist</p></div>
  <div class="box pm" style="left:510px;top:824px;width:125px;height:76px;font-size:12px"><p>Secure<br><b>Signed Scopes</b><br>from<br>Subs &amp; Vendors</p></div>
  <div class="box pm" style="left:510px;top:913px;width:125px;height:59px;font-size:11.5px"><p>On Site Meetings<br>with Customer,<br>PM &amp; Subs</p></div>
  <div class="box pm" style="left:683px;top:745px;width:476px;height:85px;border-width:7px;font-size:14px"><p><b>IN PROGRESS</b><br>Regular Communication, Job Notes,<br>Photos, Site Visits, Change Orders</p></div>

  <div class="box pm" style="left:683px;top:837px;width:133px;height:46px;font-size:12.5px"><p>Draw 2<br>Inspections / COS</p></div>
  <div class="box pm" style="left:854px;top:837px;width:133px;height:46px;font-size:12.5px"><p>Draw 3<br>Inspections / COS</p></div>
  <div class="box pm" style="left:1026px;top:837px;width:134px;height:46px;font-size:12.5px"><p>Retainage<br>Inspections / COS</p></div>
  <div class="box accounting" style="left:683px;top:892px;width:133px;height:36px;font-size:12.5px"><p>Invoice from PS</p></div>
  <div class="box accounting" style="left:854px;top:892px;width:133px;height:36px;font-size:12.5px"><p>Invoice from PS</p></div>
  <div class="box accounting" style="left:1026px;top:892px;width:134px;height:36px;font-size:12.5px"><p>Invoice from PS</p></div>
  <div class="box recon" style="left:683px;top:935px;width:133px;height:35px;font-size:9.5px"><p>Verify Docs &amp; COS Cal</p></div>
  <div class="box recon" style="left:854px;top:935px;width:133px;height:35px;font-size:9.5px"><p>Verify Docs &amp; COS Cal</p></div>
  <div class="box recon" style="left:1026px;top:935px;width:134px;height:35px;font-size:9.5px"><p>Verify Docs &amp; COS Cal</p></div>

  <div class="decision yellow" style="left:1210px;top:750px;width:100px;height:52px;font-size:9.5px">Additional<br>Scope</div>
  <span class="tag yes" style="left:1260px;top:799px;font-size:8px">Yes</span>
  <span class="tag no" style="left:1368px;top:769px;font-size:8px">No</span>
  <div class="box pm" style="left:1195px;top:812px;width:134px;height:61px"><p>Change Order/<br>Supplement</p></div>
  <div class="box recon" style="left:1195px;top:878px;width:134px;height:45px"><p>Document</p></div>
  <div class="box accounting" style="left:1195px;top:929px;width:134px;height:44px"><p>Invoice</p></div>
  <div class="decision yellow" style="left:1355px;top:794px;width:135px;height:74px;font-size:10px">Significantly<br>Complete</div>
  <span class="tag yes" style="left:1423px;top:871px;font-size:12px">Yes</span>
  <div class="box pm" style="left:1354px;top:894px;width:133px;height:60px;font-size:10px"><p>Signed<br>Punchlist</p></div>
  <div class="box pm" style="left:1517px;top:754px;width:134px;height:82px;font-size:10px"><p>Certificate of<br>Completion<br>Work Complete</p></div>
  <div class="box recon" style="left:1526px;top:859px;width:115px;height:67px;font-size:10px"><p>Submit to<br>Insurance<br>Carrier</p></div>

  <!-- Closeout -->
  <div class="box pm" style="left:206px;top:1035px;width:80px;height:71px;font-size:10px"><p>Request<br><b>Searchly</b><br><b>Review</b></p></div>
  <div class="box pm" style="left:302px;top:1035px;width:79px;height:71px;font-size:10px"><p>Final<br>Review:<br>Supplement</p></div>
  <div class="decision yellow" style="left:305px;top:1135px;width:76px;height:48px;font-size:9px">Supplement</div>
  <span class="tag no" style="left:434px;top:1108px;font-size:8px">No</span>
  <div class="box pm" style="left:472px;top:1027px;width:126px;height:76px;font-size:13px"><p>Submit<br><b>Final Invoice</b> to<br>Customer &amp; Clien</p></div>
  <div class="box estimator" style="left:472px;top:1130px;width:126px;height:77px"><p>Write Final<br>Supplement</p></div>
  <div class="box recon" style="left:660px;top:1031px;width:129px;height:74px"><p>Certificate of<br>Satisfaction</p></div>
  <div class="box recon" style="left:660px;top:1136px;width:129px;height:74px"><p>Submit to<br>Insurance Agent</p></div>
  <div class="decision teal" style="left:805px;top:1028px;width:160px;height:80px;font-size:10px">Balance Paid<br>Paid in Full</div>
  <span class="tag yes" style="left:965px;top:1070px;font-size:8px">Yes</span>
  <span class="tag no" style="left:888px;top:1110px;font-size:8px">No</span>
  <div class="box recon" style="left:977px;top:1021px;width:143px;height:84px"><p>Verify <b>Job File</b><br>is Complete</p></div>
  <div class="box accounting" style="left:1150px;top:1022px;width:143px;height:83px;font-size:12px"><p>Pay remaining<br>expenses /<br>recognize remaining<br>income.</p></div>
  <div class="box recon" style="left:1327px;top:1022px;width:144px;height:83px;font-size:12px"><p>Submit any<br>commission/bonus<br>information to<br>accounting.</p></div>
  <div class="box accounting" style="left:1499px;top:1034px;width:124px;height:62px;font-size:12px"><p>File Closed</p></div>
  <div class="box pm" style="left:821px;top:1128px;width:137px;height:82px"><p>Stay in Contact<br>with Customer<br>Awaiting Payment</p></div>
  <span class="tag" style="left:990px;top:1152px;font-size:9px">30 days</span>
  <div class="box recon" style="left:1028px;top:1130px;width:139px;height:65px;font-size:12px"><p>Certified Letter<br>Demand of Payment</p></div>
  <span class="tag" style="left:1190px;top:1146px;font-size:9px">60 days</span>
  <div class="box recon" style="left:1218px;top:1130px;width:140px;height:65px;font-size:12px"><p>Turn over to<br>Collections</p></div>
  <div class="box gm" style="left:1495px;top:1128px;width:136px;height:82px"><p><b>File Review</b><br>Gross Margin, COS,<br>Cycle Time</p></div>

  <div class="legend">
    <h2>LEGEND</h2>
    <div class="legend-item recon"><span class="swatch"></span>Recon Coordinator</div>
    <div class="legend-item accounting"><span class="swatch"></span>Accounting</div>
    <div class="legend-item estimator"><span class="swatch"></span>Estimator</div>
    <div class="legend-item pm"><span class="swatch"></span>Project Manager</div>
    <div class="legend-item gm"><span class="swatch"></span>GM/Owner</div>
    <div class="legend-item inactive"><span class="swatch"></span>Inactive Steo</div>
  </div>
</div>
</body>
</html>
```